Email Signature & Facebook Cover Design – Birchlane Study Centre

I’m looking for a clean, professional email signature and a matching Facebook cover photo for my tutoring business, Birchlane Study Centre.
The email signature needs to display properly across Outlook and iPhone without the image appearing as an attachment. It should include my logo and contact details and have a friendly but professional look suitable for an education business.
Details to include:
Moira Dunholt
Director & Lead Tutor
Birchlane Study Centre
hello@birchlanestudy.co.uk
www.birchlanestudy.co.uk
01632 418736
The Facebook cover should match the branding, feel professional and welcoming, and be optimised for desktop and mobile.

```html
<!DOCTYPE html>
<html lang="en">
<head>
<meta charset="utf-8">
<title>Birchlane Study Centre – Email Signature &amp; Facebook Cover</title>
<link rel="stylesheet" href="https://fonts.googleapis.com/css2?family=Fira+Sans:wght@400;600&family=Figtree:ital,wght@0,400;1,800&family=Inter:wght@400&display=swap">
<style>
  :root {
    --paper: #ffffff;
    --cream: #f0efe8;
    --brand-green: #4bb86b;
    --brand-green-deep: #46ad64;
    --ink: #141414;
    --white: #ffffff;
  }
  * { box-sizing: border-box; margin: 0; padding: 0; }
  html, body {
    width: 1009px; height: 1200px; overflow: hidden;
    background: var(--paper);
  }
  .sheet { position: relative; width: 1009px; height: 1200px; }

  .section-label {
    position: absolute; left: 72px;
    font-family: "Inter", Arial, sans-serif;
    font-size: 25px; font-weight: 400; color: var(--ink); letter-spacing: -0.2px;
    line-height: 30px;
  }
  .section-label--signature { top: 38px; }
  .section-label--cover { top: 581px; }

  .panel {
    position: absolute; left: 73px; width: 858px;
    background: var(--cream); overflow: hidden;
  }
  .panel--signature { top: 87px; height: 429px; }
  .panel--cover { top: 631px; height: 498px; }

  .brand-tab {
    position: absolute; top: 0;
    background: var(--brand-green);
    overflow: hidden;
    display: flex; align-items: center; justify-content: center;
    text-align: center;
  }
  .brand-tab::after {
    content: ""; position: absolute;
    border-radius: 50%;
    background: var(--brand-green-deep);
  }
  .panel--signature .brand-tab {
    left: 47px; width: 291px; height: 379px;
    border-radius: 0 0 146px 146px;
  }
  .panel--signature .brand-tab::after {
    width: 360px; height: 360px; left: 150px; top: 190px;
  }
  .panel--cover .brand-tab {
    left: 87px; width: 198px; height: 235px;
    border-radius: 0 0 99px 99px;
  }
  .panel--cover .brand-tab::after {
    width: 250px; height: 250px; left: 100px; top: 110px;
  }
  .brand-name {
    position: relative; z-index: 1;
    font-family: "Fira Sans", Arial, sans-serif;
    font-weight: 600; color: var(--white);
    line-height: 1.05;
  }
  .panel--signature .brand-name { font-size: 40px; margin-top: 40px; }
  .panel--cover .brand-name { font-size: 28px; margin-top: 10px; }

  .contact-card {
    position: absolute; left: 415px; top: 83px;
    font-family: "Fira Sans", Arial, sans-serif;
    color: var(--ink);
  }
  .contact-card__name {
    font-size: 29px; font-weight: 600; color: var(--brand-green);
    line-height: 36px;
  }
  .contact-card__role {
    font-size: 23px; line-height: 35px; margin-top: 3px;
  }
  .contact-list { list-style: none; margin-top: 24px; }
  .contact-list li {
    display: flex; align-items: center;
    height: 42px; font-size: 23px; letter-spacing: 0.2px;
  }
  .contact-icon {
    width: 36px; height: 36px; border-radius: 50%;
    background: var(--brand-green);
    display: flex; align-items: center; justify-content: center;
    margin-right: 13px; flex: none;
  }
  .contact-icon svg { width: 20px; height: 20px; }

  .cover-tagline {
    position: absolute; left: 88px; top: 258px;
    font-family: "Figtree", Arial, sans-serif;
    font-size: 32px; line-height: 36px; color: var(--ink);
    font-weight: 400;
  }
  .cover-tagline em { font-style: italic; font-weight: 800; }

  .cover-circle {
    position: absolute; left: 466px; top: 108px;
    width: 430px; height: 430px; border-radius: 50%;
    background: var(--brand-green);
  }
  .cover-photo {
    position: absolute; left: 417px; top: 46px;
    width: 420px; height: 452px;
    border-radius: 180px 180px 0 0;
    background: linear-gradient(170deg, #5a3b2c 0%, #c79872 38%, #b97a45 62%, #8a8480 100%);
  }
</style>
</head>
<body>
<main class="sheet">

  <h2 class="section-label section-label--signature">email signature</h2>

  <section class="panel panel--signature" aria-label="Email signature">
    <div class="brand-tab">
      <p class="brand-name">Birchlane<br>Study<br>Centre</p>
    </div>

    <div class="contact-card">
      <p class="contact-card__name">Moira Dunholt</p>
      <p class="contact-card__role">Director &amp; Lead Tutor<br>Birchlane Study Centre</p>
      <ul class="contact-list">
        <li>
          <span class="contact-icon">
            <svg viewBox="0 0 20 20" fill="none" stroke="#fff" stroke-width="1.6">
              <rect x="2.5" y="4.5" width="15" height="11" rx="1"/>
              <path d="M2.5 4.5l7.5 6 7.5-6M2.5 15.5l5.5-5M17.5 15.5l-5.5-5"/>
            </svg>
          </span>
          hello@birchlanestudy.co.uk
        </li>
        <li>
          <span class="contact-icon">
            <svg viewBox="0 0 20 20" fill="none" stroke="#fff" stroke-width="1.4">
              <circle cx="10" cy="10" r="7.5"/>
              <ellipse cx="10" cy="10" rx="3.4" ry="7.5"/>
              <path d="M2.5 10h15M4 6h12M4 14h12M10 2.5v15"/>
            </svg>
          </span>
          www.birchlanestudy.co.uk
        </li>
        <li>
          <span class="contact-icon">
            <svg viewBox="0 0 20 20" fill="#fff">
              <path d="M5.2 2.8l2.4 3.1-1.4 1.8c.9 2.2 2.6 3.9 4.8 4.8l1.8-1.4 3.1 2.4-1.3 2.6c-5.6-.3-10-4.7-10.3-10.3z"/>
              <path d="M11.5 4.5a4 4 0 0 1 4 4M11.5 1.8a6.7 6.7 0 0 1 6.7 6.7" fill="none" stroke="#fff" stroke-width="1.2"/>
            </svg>
          </span>
          01632 418736
        </li>
      </ul>
    </div>
  </section>

  <h2 class="section-label section-label--cover">Facebook Cover</h2>

  <section class="panel panel--cover" aria-label="Facebook cover">
    <div class="brand-tab">
      <p class="brand-name">Birchlane<br>Study<br>Centre</p>
    </div>

    <p class="cover-tagline">Lessons that<br><em>land</em>, progress that<br>really <em>lasts</em>.</p>

    <div class="cover-circle"></div>
    <div class="cover-photo" role="img" aria-label="Photo of a smiling young student in a tan shirt holding an open laptop"></div>
  </section>

</main>
</body>
</html>
```